Real Estate Seller Financing Postcard

I need a postcard that lays out these options contained in the notes that grabs attention, explains the two options easily and is eye-catching. The front needs to have the percentages on it and information about it and on the other side One side exact Text is:
"Monthly income without tenant headaches" in big letters. Also on front "Get
110%
add an "or"
160% of market value for your property. ". The percentages should be displayed and that is not to be a sentence of text. Other side text: I need bullets points for these "Formal protection as a lien holder against home
No commission or closing cost
Fast closings possible
Property taken as is so no repairs.

Add to the top of the back in "It’s simple. I am a new investor without down payment capital who still want to double our portfolio this year to grow our portfolio."
Here are the two options that are to be the largest part of the back
Option 1, you can receive 80% now cash and 30% over a short period of time including interest.

Option 2, where act like a bank allowing you to make 150% if you finance the whole property(ies). No gimmicks and surprises, just simple unconventional financing.

Include Logo Somewhere

Target Market(s)

Property Owners Wanting to Sell Their Property

Industry/Entity Type

Real Estate Investing

Requirements
Must have
• The options promiment and each side with its respective information. Must have logo somewhere
Nice to have
• The options in color other than black.
Should not have
• A picture of money on the front. Any other image is okay.

```html
<!DOCTYPE html>
<html lang="en">
<head>
<meta charset="utf-8">
<title>Seller Financing Postcard</title>
<link rel="stylesheet" href="https://fonts.googleapis.com/css2?family=Roboto:wght@400;500;700&display=swap">
<style>
  :root{
    --blue:#1f4fa6;
    --navy:#0e3b8c;
    --sky:#3f8de0;
    --grey:#8c8c8c;
    --ink:#0b0b0b;
    --paper:#ffffff;
    --text-dark:#1c1c1c;
    --canvas:#ffffff;
  }
  *{box-sizing:border-box;margin:0;padding:0}
  html,body{width:1200px;height:2400px;overflow:hidden;background:var(--canvas)}
  body{position:relative;font-family:'Roboto',Arial,sans-serif}
  .card{position:absolute;left:168px;width:816px;height:544px;background:var(--paper);overflow:hidden;box-shadow:0 6px 18px rgba(0,0,0,.28)}
  .card--front{top:616px}
  .card--back{top:1240px}
  .card svg.shapes{position:absolute;inset:0}
  .abs{position:absolute}

  /* front */
  .hero-photo{position:absolute;left:200px;top:0;width:616px;height:487px;
    background:linear-gradient(90deg,rgba(255,255,255,1) 0%,#dfe7ee 25%,#c3d2df 50%,#e9eef2 75%,#b9c3cc 100%)}
  .brand{display:flex;align-items:center;gap:10px;color:var(--navy)}
  .brand__mark{width:60px;height:60px;border:2px solid var(--navy);border-radius:50%}
  .brand__name{font-weight:500;line-height:1;letter-spacing:1px}
  .brand__name span{display:block;font-size:.43em;letter-spacing:1px;margin-top:3px}
  .front-brand{left:34px;top:46px;font-size:28px}
  .headline{left:31px;top:168px;color:#fff;font-size:17px}
  .get{left:30px;top:216px;color:#fff;font-size:66px;font-weight:700;line-height:1}
  .pct-box{left:179px;top:214px;width:387px;height:64px;border:1.5px dashed rgba(255,255,255,.85);display:flex;align-items:center;color:#fff}
  .pct-box b{flex:1;text-align:center;font-size:37px;font-weight:700}
  .pct-box i{width:1px;height:38px;background:rgba(255,255,255,.7)}
  .market{left:32px;top:315px;color:#fff;font-size:15px;line-height:18px;width:640px}
  .market big{font-size:20px}
  .bullets{left:0;top:390px;height:67px;width:700px;display:flex;align-items:center}
  .bullet{display:flex;align-items:center;gap:14px;font-size:15px;font-weight:500;color:var(--text-dark);line-height:18px}
  .bullet svg{flex:none}
  .bullet-sep{width:2px;height:50px;background:var(--ink)}
  .footer-call{left:35px;top:487px;height:57px;display:flex;align-items:center;gap:22px}
  .call-label{color:var(--sky);font-size:26px;font-weight:700}
  .phone{display:flex;align-items:center;gap:10px;color:#fff;font-size:28px}
  .web{display:flex;align-items:center;gap:18px;color:#fff;font-size:15px;letter-spacing:1.2px}
  .front-web{left:432px;top:487px;height:57px}

  /* back */
  .quote{left:31px;top:30px;width:290px;color:#fff;font-size:17px;font-weight:500;line-height:20.5px}
  .option-tab{left:43px;font-size:24px;font-weight:700;color:var(--ink);height:36px;line-height:36px}
  .option-text{left:32px;color:#fff;font-size:15px;font-weight:500;line-height:19px}
  .option-text b{font-size:22px;font-weight:500}
  .call-badge{left:28px;top:457px;width:85px;height:28px;background:var(--ink);color:var(--sky);font-size:16px;font-weight:700;text-align:center;line-height:28px}
  .back-phone{left:35px;top:486px;height:58px}
  .back-web{left:260px;top:486px;height:58px;letter-spacing:.3px;font-size:16px;gap:10px}
  .back-brand{left:507px;top:112px;font-size:21px;gap:6px}
  .back-brand .brand__mark{width:44px;height:44px}
  .stamp{left:672px;top:99px;width:67px;height:72px;border:1px solid #555}
  .address-line{left:515px;width:224px;height:1px;background:#333}
</style>
</head>
<body>

<section class="card card--front" aria-label="Postcard front">
  <div class="hero-photo" role="img" aria-label="Photo of an investor working at a laptop on a bright desk with potted cacti"></div>
  <svg class="shapes" width="816" height="544" viewBox="0 0 816 544">
    <polygon points="0,140 610,140 620,152 0,152" fill="var(--grey)"/>
    <polygon points="0,150 616,150 816,440 816,487 0,487" fill="var(--blue)"/>
    <polygon points="0,390 690,390 730,457 0,457" fill="var(--paper)"/>
    <polygon points="690,390 716,390 758,456 732,456" fill="var(--ink)"/>
    <polygon points="0,487 392,487 414,544 0,544" fill="var(--ink)"/>
    <polygon points="392,487 816,487 816,544 414,544" fill="var(--grey)"/>
    <polygon points="790,487 816,487 816,544" fill="#555"/>
  </svg>

  <div class="abs brand front-brand">
    <div class="brand__mark"></div>
    <div class="brand__name">HALCYON<span>REAL ESTATE GROUP</span></div>
  </div>

  <p class="abs headline">"Monthly income without tenant headaches" in big letters. Also on front</p>
  <p class="abs get">GET</p>
  <div class="abs pct-box"><b>100%</b><i></i><b>110%</b><i></i><b>160%</b></div>
  <p class="abs market"><big>of market value for your property.</big> " .The percentages should be displayed and that is not to be a sentence of text. Other side text: I need bullets points for these "Formal protection as a lien holder against home</p>

  <div class="abs bullets">
    <div class="bullet" style="margin-left:38px;width:190px">
      <svg width="28" height="26" viewBox="0 0 28 26"><rect x="2" y="5" width="19" height="19" rx="3" fill="none" stroke="var(--blue)" stroke-width="2.5"/><path d="M7 13l5 5L26 2" fill="none" stroke="var(--blue)" stroke-width="3"/></svg>
      <span>No commission or<br>closing cost</span>
    </div>
    <div class="bullet-sep"></div>
    <div class="bullet" style="margin-left:33px;width:165px">
      <svg width="28" height="26" viewBox="0 0 28 26"><rect x="2" y="5" width="19" height="19" rx="3" fill="none" stroke="var(--blue)" stroke-width="2.5"/><path d="M7 13l5 5L26 2" fill="none" stroke="var(--blue)" stroke-width="3"/></svg>
      <span>Fast closings<br>possible</span>
    </div>
    <div class="bullet-sep"></div>
    <div class="bullet" style="margin-left:30px">
      <svg width="28" height="26" viewBox="0 0 28 26"><rect x="2" y="5" width="19" height="19" rx="3" fill="none" stroke="var(--blue)" stroke-width="2.5"/><path d="M7 13l5 5L26 2" fill="none" stroke="var(--blue)" stroke-width="3"/></svg>
      <span>Property taken as is so<br>no repairs.</span>
    </div>
  </div>

  <div class="abs footer-call">
    <span class="call-label">CALL US</span>
    <span class="phone">
      <svg width="22" height="22" viewBox="0 0 24 24"><path d="M6.6 10.8a15 15 0 0 0 6.6 6.6l2.2-2.2a1 1 0 0 1 1-.25 11.4 11.4 0 0 0 3.6.57 1 1 0 0 1 1 1V20a1 1 0 0 1-1 1A17 17 0 0 1 3 4a1 1 0 0 1 1-1h3.5a1 1 0 0 1 1 1c0 1.25.2 2.45.57 3.57a1 1 0 0 1-.25 1z" fill="#fff"/></svg>
      1234567890
    </span>
  </div>
  <div class="abs web front-web">
    <svg width="20" height="20" viewBox="0 0 20 20"><circle cx="10" cy="10" r="9" fill="var(--blue)"/><path d="M1 10h18M10 1v18M3 5h14M3 15h14" stroke="#fff" stroke-width="1" fill="none"/><ellipse cx="10" cy="10" rx="4" ry="9" stroke="#fff" fill="none"/></svg>
    www.yourwebsitethere.com
  </div>
</section>

<section class="card card--back" aria-label="Postcard back">
  <svg class="shapes" width="816" height="544" viewBox="0 0 816 544">
    <polygon points="0,0 280,0 415,231 397,291 0,291" fill="var(--grey)"/>
    <polygon points="280,0 287,0 422,231 415,231" fill="var(--navy)"/>
    <polygon points="0,152 317,152 511,486 0,486" fill="var(--blue)"/>
    <polygon points="0,177 210,177 224,213 0,213" fill="var(--paper)"/>
    <polygon points="0,322 208,322 222,358 0,358" fill="var(--paper)"/>
    <polygon points="0,486 511,486 496,544 0,544" fill="var(--ink)"/>
  </svg>

  <p class="abs quote">"It’s simple. I am a new investor without down payment capital who still want to double our port-folio this year to grow our portfo-lio."</p>

  <p class="abs option-tab" style="top:177px">OPTION 1</p>
  <p class="abs option-text" style="top:244px">you can receive <b>80%</b> now cash and <b>30%</b><br>over a short period of time including interest.</p>

  <p class="abs option-tab" style="top:322px;left:46px">OPTION 2</p>
  <p class="abs option-text" style="top:383px;left:29px">where act like a bank allowing you to make <b>150%</b> if you fi-<br>nance the whole property(ies). No gimmicks and surprises,<br>just simple unconventional financing.</p>

  <div class="abs call-badge">CALL US</div>
  <div class="abs phone back-phone">
    <svg width="22" height="22" viewBox="0 0 24 24"><path d="M6.6 10.8a15 15 0 0 0 6.6 6.6l2.2-2.2a1 1 0 0 1 1-.25 11.4 11.4 0 0 0 3.6.57 1 1 0 0 1 1 1V20a1 1 0 0 1-1 1A17 17 0 0 1 3 4a1 1 0 0 1 1-1h3.5a1 1 0 0 1 1 1c0 1.25.2 2.45.57 3.57a1 1 0 0 1-.25 1z" fill="#fff"/></svg>
    <span style="margin-left:8px">1234567890</span>
  </div>
  <div class="abs web back-web">
    <svg width="20" height="20" viewBox="0 0 20 20"><circle cx="10" cy="10" r="9" fill="var(--blue)"/><path d="M1 10h18M10 1v18M3 5h14M3 15h14" stroke="#fff" stroke-width="1" fill="none"/><ellipse cx="10" cy="10" rx="4" ry="9" stroke="#fff" fill="none"/></svg>
    www.yourwebsitethere.com
  </div>

  <div class="abs brand back-brand">
    <div class="brand__mark"></div>
    <div class="brand__name">HALCYON<span>REAL ESTATE GROUP</span></div>
  </div>
  <div class="abs stamp"></div>
  <div class="abs address-line" style="top:199px"></div>
  <div class="abs address-line" style="top:240px"></div>
  <div class="abs address-line" style="top:282px"></div>
</section>

</body>
</html>
```